Orlow Wellness Group Website

Need a informative, detailed and functional website for a medical cannabis clinic website

check out www.tesmorahealthcare.com as competition - want better site than they have

Target Market(s)

Patients

Industry/Entity Type

Health Care

Number of Pages Required

1 page

Font styles to use
Sans Serif

Colors
cadf82
abd036
9bcb3b
3276b5
33a6d7
0392cd
f68d4e

Requirements
Must have
• Clean / Informative
• Will add additional educational content on opioid reduction
Nice to have
• like the white contrast with black/slate dividers. Green logo looks good on slate
• Check documents for ppt regarding website ideas
Should not have
• too many words

```html
<!DOCTYPE html>
<html lang="en">
<head>
<meta charset="utf-8">
<title>Arkansas Orlow Wellness Group</title>
<link rel="stylesheet" href="https://fonts.googleapis.com/css2?family=Montserrat:wght@400;500;600;700&family=Open+Sans:wght@400;600&display=swap">
<style>
:root{
  --green:#9bcb3b;
  --green-light:#cadf82;
  --green-mid:#abd036;
  --slate:#2f3030;
  --slate-dark:#262727;
  --ink:#1f1f1f;
  --body:#555;
  --panel:#f3f3f3;
  --white:#fff;
}
*{margin:0;padding:0;box-sizing:border-box}
html,body{width:1200px;height:4072px;overflow:hidden}
body{position:relative;background:var(--white);font-family:"Open Sans",Arial,sans-serif;color:var(--body);font-size:14px;line-height:1.75}
h1,h2,h3,h4,.btn,.nav a,.eyebrow{font-family:"Montserrat",Arial,sans-serif}
.abs{position:absolute}
.btn{position:absolute;display:flex;align-items:center;justify-content:center;background:var(--green);color:var(--white);border-radius:26px;font-size:15px;font-weight:500;text-decoration:none}
.center{text-align:center}

/* header */
.site-header{position:absolute;left:0;top:0;width:1200px;height:77px;background:var(--white);z-index:2}
.logo{position:absolute;left:165px;top:14px;display:flex;align-items:center;gap:12px}
.logo-dot{width:46px;height:46px;border-radius:50%;background:var(--green)}
.logo-name{font-family:"Montserrat",sans-serif;font-weight:600;font-size:14px;line-height:1.15;color:var(--green);letter-spacing:2px;text-transform:uppercase}
.nav a{position:absolute;top:26px;color:#444;text-decoration:none;font-size:13px;line-height:1;white-space:nowrap}
.search{position:absolute;left:1022px;top:20px;width:38px;height:38px;border:2px solid #333;border-radius:50%}
.search::after{content:"";position:absolute;left:9px;top:8px;width:12px;height:12px;border:2px solid #333;border-radius:50%}

/* hero */
.hero-photo{position:absolute;left:0;top:77px;width:1200px;height:513px;background:radial-gradient(ellipse at 62% 20%,#fff4c2 0%,#f7b33a 18%,#d86a1c 42%,#7a4a1e 68%,#3b4a1e 100%)}
.hero-copy{position:absolute;left:184px;top:200px;color:var(--white)}
.hero-copy .eyebrow{font-size:15px;letter-spacing:1px;text-transform:uppercase}
.hero-copy h1{font-size:40px;font-weight:700;letter-spacing:1px;margin-top:8px}
.hero-copy p{font-size:14px;margin-top:6px;width:470px;line-height:1.6}

/* steps strip */
.steps{position:absolute;left:146px;top:640px;width:912px;height:315px;background:var(--panel)}
.step{position:absolute;top:0;width:304px;height:315px;text-align:center;padding:45px 34px 0}
.step h3{font-size:18px;font-weight:600;color:var(--ink)}
.step .ico{width:88px;height:88px;border-radius:50%;margin:26px auto 22px;background:var(--green);border:5px solid #d9e9b4;display:flex;align-items:center;justify-content:center}
.step p{font-size:13px;line-height:1.7}
.step.active{background:linear-gradient(160deg,#a8d44a,#8cc13a);color:var(--white)}
.step.active h3{color:var(--white)}
.step.active .ico{background:var(--white);border-color:#c9e58b}
.step-divider{position:absolute;top:0;left:608px;width:1px;height:315px;background:#ddd}

/* intro */
.divider-mark{position:absolute;left:525px;width:150px;height:20px}
.intro h2{position:absolute;left:0;top:1068px;width:1200px;text-align:center;font-size:33px;font-weight:600;letter-spacing:1px;color:var(--ink)}
.intro h2 span{color:var(--green)}
.intro p{position:absolute;left:170px;top:1130px;width:860px;text-align:center;font-size:13px;line-height:2.2}

/* process */
.process{position:absolute;left:0;top:1410px;width:1200px;height:725px;background:linear-gradient(180deg,var(--slate),var(--slate-dark))}
.process h2{position:absolute;left:0;top:125px;width:1200px;text-align:center;color:var(--white);font-size:24px;font-weight:600}
.process .lede{position:absolute;left:220px;top:172px;width:760px;text-align:center;color:#ddd;font-size:13px;line-height:2.2}
.process-line{position:absolute;left:250px;top:401px;width:700px;height:2px;background:#555}
.stage{position:absolute;top:290px;width:300px;text-align:center}
.stage .ring{width:222px;height:222px;margin:0 auto;border-radius:50%;background:var(--green);border:10px solid #e4f0c6;display:flex;align-items:center;justify-content:center;position:relative}
.stage .badge{position:absolute;right:4px;top:6px;width:38px;height:38px;border-radius:50%;background:var(--slate-dark);display:flex;align-items:center;justify-content:center}
.stage h3{color:var(--white);font-size:16px;font-weight:600;line-height:1.7;margin-top:22px}
.stage p{color:#ddd;font-size:12.5px;line-height:1.8;margin-top:14px;padding:0 20px}

/* benefits */
.benefit-photo{position:absolute;left:143px;top:2252px;width:379px;height:426px;border:4px solid var(--green);padding:12px;background:var(--white)}
.benefit-photo div{width:100%;height:100%;background:radial-gradient(ellipse at 30% 20%,#fff6c8,#e7b83a 35%,#8e8a24 65%,#4a5a1a)}
.benefits .eyebrow{position:absolute;left:573px;top:2212px;font-size:15px;letter-spacing:1px;text-transform:uppercase;color:#444}
.benefits h2{position:absolute;left:573px;top:2240px;font-size:30px;font-weight:600;color:var(--ink)}
.perk{position:absolute;width:230px}
.perk .dot{width:52px;height:52px;border-radius:50%;background:var(--green);border:4px solid #dcebb8;display:flex;align-items:center;justify-content:center}
.perk h4{font-size:15px;font-weight:600;color:var(--ink);margin-top:12px}
.perk p{font-size:12.5px;line-height:1.7;margin-top:10px}

/* doctor banner */
.doctor-band{position:absolute;left:0;top:2760px;width:1200px;height:280px;background:linear-gradient(180deg,#3f4a38,#27301f 55%,#3a4232)}
.doctor-band h2{position:absolute;left:0;top:100px;width:1200px;text-align:center;color:var(--white);font-size:32px;font-weight:600;letter-spacing:1px}

/* network */
.network h2{position:absolute;left:0;top:3155px;width:1200px;text-align:center;font-size:23px;font-weight:700;color:var(--ink)}
.network .lede{position:absolute;left:240px;top:3200px;width:720px;text-align:center;font-size:13px;line-height:2}
.card{position:absolute;top:3300px;width:283px;height:325px;background:var(--panel)}
.card .photo{height:174px;background:linear-gradient(150deg,#2f5a1c,#6fa83a 50%,#1f3a12)}
.card h3{font-size:15px;font-weight:700;color:var(--ink);text-align:center;margin-top:30px}
.card p{font-size:12.5px;text-align:center;line-height:1.7;margin-top:16px;padding:0 30px}

/* footer */
.site-footer{position:absolute;left:0;top:3680px;width:1200px;height:310px;background:linear-gradient(160deg,#3a4136,#2c3129 60%,#3b4238);color:#ddd}
.site-footer h4{position:absolute;top:52px;color:var(--white);font-size:16px;font-weight:600}
.foot-logo{position:absolute;left:150px;top:62px;display:flex;align-items:center;gap:12px}
.foot-logo .logo-name{color:var(--white)}
.foot-about{position:absolute;left:150px;top:175px;width:215px;font-size:12px;line-height:1.7}
.links{position:absolute;left:410px;top:95px;list-style:none;font-size:12.5px;line-height:2.1}
.links li::before{content:"› ";color:var(--green)}
.contact{position:absolute;left:550px;top:100px;font-size:12.5px}
.contact div{display:flex;align-items:center;gap:14px;margin-bottom:22px}
.field{position:absolute;height:32px;background:#5e625b;color:#eee;font-size:11px;padding:6px 10px}
.subscribe{position:absolute;left:788px;top:270px;width:90px;height:30px;border-radius:16px;background:var(--green);color:var(--white);font-family:"Montserrat",sans-serif;font-size:12px;display:flex;align-items:center;justify-content:center}
.bottom-bar{position:absolute;left:0;top:3990px;width:1200px;height:82px;background:var(--white)}
.bottom-bar p{position:absolute;left:150px;top:30px;font-size:12.5px;color:#333}
.social{position:absolute;top:24px;width:32px;height:32px;border-radius:50%;background:var(--green)}
</style>
</head>
<body>

<header class="site-header">
  <div class="logo"><span class="logo-dot"></span><span class="logo-name">Arkansas<br>Orlow Wellness<br>Group</span></div>
  <nav class="nav">
    <a style="left:434px">Home</a>
    <a style="left:511px">About</a>
    <a style="left:593px">Qualify</a>
    <a style="left:681px">Appointments</a>
    <a style="left:807px">FAQ</a>
    <a style="left:876px">News</a>
    <a style="left:946px">Contact</a>
  </nav>
  <span class="search"></span>
</header>

<section class="hero">
  <div class="hero-photo" role="img" aria-label="Woman with open arms in a hillside field at sunset"></div>
  <div class="hero-copy">
    <div class="eyebrow">We help cannabis</div>
    <h1>ARKANSAS MEDICAL</h1>
    <p>Lorem ipsum dolor sit amet, consectetur adipiscing elit, sed do eiusmod tempor incididunt ut labore et dolore magna aliqua.</p>
  </div>
  <a class="btn" style="left:184px;top:376px;width:182px;height:52px">Book Appointment</a>
</section>

<section class="steps">
  <div class="step active" style="left:0" role="img" aria-label="Green leaf backdrop">
    <h3>Meet a Arkansas Doctor</h3>
    <div class="ico"><svg width="40" height="40" viewBox="0 0 40 40" fill="none" stroke="#9bcb3b" stroke-width="2.5"><rect x="9" y="6" width="22" height="28" rx="2"/><path d="M14 15h12M14 21h12M14 27h8"/></svg></div>
    <p>Lorem ipsum dolor sit amet, consectetur adipiscing elit, sed do eiusmod tempor incididunt ut labore</p>
  </div>
  <div class="step" style="left:304px">
    <h3>Apply for Arkansas Card</h3>
    <div class="ico"><svg width="40" height="40" viewBox="0 0 40 40" fill="none" stroke="#fff" stroke-width="2.5"><rect x="6" y="10" width="28" height="20" rx="2"/><path d="M12 20l4 4 8-8"/></svg></div>
    <p>Lorem ipsum dolor sit amet, consectetur adipiscing elit, sed do eiusmod tempor incididunt ut labore</p>
  </div>
  <div class="step-divider"></div>
  <div class="step" style="left:608px">
    <h3>Follow-up Appointment</h3>
    <div class="ico"><svg width="40" height="40" viewBox="0 0 40 40" fill="none" stroke="#fff" stroke-width="2.5"><circle cx="20" cy="20" r="13"/><path d="M16 16a4 4 0 1 1 5 4v3M20 27v1"/></svg></div>
    <p>Lorem ipsum dolor sit amet, consectetur adipiscing elit, sed do eiusmod tempor incididunt ut labore</p>
  </div>
  <svg class="abs" style="left:250px;top:110px" width="420" height="70" viewBox="0 0 420 70" fill="none" stroke="#333" stroke-width="1.5">
    <path d="M0 40 Q40 0 90 30"/><path d="M82 22l8 8-11 2"/>
    <path d="M330 40 Q370 0 420 30"/><path d="M412 22l8 8-11 2"/>
  </svg>
</section>

<section class="intro">
  <svg class="divider-mark" style="top:1025px" viewBox="0 0 150 20"><path d="M0 10h60M90 10h60" stroke="#9bcb3b" stroke-width="1.5"/><circle cx="75" cy="10" r="7" fill="#9bcb3b"/></svg>
  <h2>ARKANSAS <span>ORLOW WELLNESS GROUP</span></h2>
  <p>Lorem ipsum dolor sit amet, consectetur adipiscing elit, sed do eiusmod tempor incididunt ut labore et dolore magna aliqua. Ut enim ad minim veniam, quis nostrud exercitation ullamco laboris nisi ut aliquip ex ea commodo consequat. Duis aute irure dolor in reprehenderit in voluptate velit esse cillum dolore eu fugiat nulla pariatur. Excepteur sint occaecat cupidatat non proident, sunt in culpa qui officia deserunt mollit anim id est laborum</p>
  <a class="btn" style="left:522px;top:1293px;width:157px;height:50px">More Info</a>
</section>

<section class="process">
  <svg class="divider-mark" style="top:72px" viewBox="0 0 150 20"><path d="M0 10h60M90 10h60" stroke="#9bcb3b" stroke-width="1.5"/><circle cx="75" cy="10" r="7" fill="#9bcb3b"/></svg>
  <h2>Application &amp; Approval - In 3 Easy Steps</h2>
  <p class="lede">Lorem ipsum dolor sit amet, consectetur adipiscing elit, sed do eiusmod tempor incididunt ut labore et dolore magna aliqua. Ut enim ad minim veniam, quis nostrud exercitation ullamco laboris nisi</p>
  <div class="process-line"></div>
  <div class="stage" style="left:160px">
    <div class="ring">
      <span class="badge"><svg width="16" height="16" viewBox="0 0 16 16" fill="none" stroke="#fff" stroke-width="2"><path d="M8 2v10M4 8l4 4 4-4"/></svg></span>
      <svg width="90" height="90" viewBox="0 0 90 90" fill="none" stroke="#fff" stroke-width="3"><rect x="22" y="14" width="40" height="56" rx="3"/><rect x="30" y="20" width="40" height="56" rx="3" fill="#9bcb3b"/><path d="M38 36h24M38 48h24M38 60h16"/></svg>
    </div>
    <h3>Complete Your applicaition<br>Here Online</h3>
    <p>Lorem ipsum dolor sit amet, consectetur adipiscing elit, sed do eiusmod incididunt ut labore et dolore magna aliqua Ut enim ad minim veniam, quis</p>
  </div>
  <div class="stage" style="left:450px">
    <div class="ring">
      <span class="badge"><svg width="16" height="16" viewBox="0 0 16 16" fill="none" stroke="#fff" stroke-width="2"><path d="M8 2v10M4 8l4 4 4-4"/></svg></span>
      <svg width="90" height="90" viewBox="0 0 90 90" fill="none" stroke="#fff" stroke-width="3"><rect x="24" y="14" width="42" height="60" rx="3"/><rect x="36" y="9" width="18" height="10" rx="2" fill="#9bcb3b"/><path d="M34 44l8 8 16-16"/></svg>
    </div>
    <h3>Get a Doctor's<br>Recommendation</h3>
    <p>Lorem ipsum dolor sit amet, consectetur adipiscing elit, sed do eiusmod incididunt ut labore et dolore magna aliqua Ut enim ad minim veniam, quis</p>
  </div>
  <div class="stage" style="left:756px">
    <div class="ring">
      <span class="badge"><svg width="16" height="16" viewBox="0 0 16 16" fill="none" stroke="#fff" stroke-width="2"><path d="M8 2v10M4 8l4 4 4-4"/></svg></span>
      <svg width="90" height="90" viewBox="0 0 90 90" fill="none" stroke="#fff" stroke-width="3"><rect x="14" y="26" width="62" height="46" rx="4"/><path d="M34 26v-8h22v8"/><path d="M45 38v22M34 49h22" stroke-width="6"/></svg>
    </div>
    <h3>Getting Medical<br>Marijuana</h3>
    <p>Lorem ipsum dolor sit amet, consectetur adipiscing elit, sed do eiusmod incididunt ut labore et dolore magna aliqua Ut enim ad minim veniam, quis</p>
  </div>
</section>

<section class="benefits">
  <div class="benefit-photo"><div role="img" aria-label="Cannabis plant backlit by golden sunlight"></div></div>
  <div class="eyebrow">Benefits you get with</div>
  <h2>Arkansas Medical Cannabis</h2>
  <div class="perk" style="left:568px;top:2328px"><span class="dot"><svg width="22" height="22" viewBox="0 0 22 22" fill="none" stroke="#fff" stroke-width="2.5"><path d="M4 11l5 5 9-10"/></svg></span><h4>Meet a Arkansa Doctor</h4><p>Lorem ipsum dolor sit amet, consectetur adipiscing elit, sed do eiusmod tempor</p></div>
  <div class="perk" style="left:820px;top:2328px"><span class="dot"><svg width="22" height="22" viewBox="0 0 22 22" fill="none" stroke="#fff" stroke-width="2.5"><path d="M4 11l5 5 9-10"/></svg></span><h4>Apply For Card</h4><p>Lorem ipsum dolor sit amet, consectetur adipiscing elit, sed do eiusmod tempor</p></div>
  <div class="perk" style="left:568px;top:2520px"><span class="dot"><svg width="22" height="22" viewBox="0 0 22 22" fill="none" stroke="#fff" stroke-width="2.5"><path d="M4 11l5 5 9-10"/></svg></span><h4>Follow Up Appointment</h4><p>Lorem ipsum dolor sit amet, consectetur adipiscing elit, sed do eiusmod tempor</p></div>
  <div class="perk" style="left:820px;top:2520px"><span class="dot"><svg width="22" height="22" viewBox="0 0 22 22" fill="none" stroke="#fff" stroke-width="2.5"><path d="M4 11l5 5 9-10"/></svg></span><h4>Lorem Ipsum</h4><p>Lorem ipsum dolor sit amet, consectetur adipiscing elit, sed do eiusmod tempor</p></div>
</section>

<section class="doctor-band" role="img" aria-label="Dark cannabis leaves backdrop">
  <svg class="divider-mark" style="top:50px" viewBox="0 0 150 20"><path d="M0 10h60M90 10h60" stroke="#9bcb3b" stroke-width="1.5"/><circle cx="75" cy="10" r="7" fill="#9bcb3b"/></svg>
  <h2>MEET OUR ARKANSAS MEDICAL DOCTOR</h2>
  <a class="btn" style="left:531px;top:188px;width:138px;height:40px;font-size:12px">Book Appointment</a>
</section>

<section class="network">
  <svg class="divider-mark" style="top:3102px" viewBox="0 0 150 20"><path d="M0 10h60M90 10h60" stroke="#9bcb3b" stroke-width="1.5"/><circle cx="75" cy="10" r="7" fill="#9bcb3b"/></svg>
  <h2>Little Rock's First and Only Specialized Arkasnsas Medical Network</h2>
  <p class="lede">Lorem ipsum dolor sit amet, consectetur adipiscing elit, sed do eiusmod tempor incididunt ut labore et dolore magna aliqua. Ut enim ad minim veniam, quis nostrud exercitation ullamco laboris nisi</p>
  <div class="card" style="left:143px"><div class="photo" role="img" aria-label="Cannabis leaves close-up"></div><h3>No Qualification? No Fee.</h3><p>Lorem ipsum dolor sit amet, consectetur adipiscing elit, sed do eiusmod tempor incididunt</p></div>
  <div class="card" style="left:460px"><div class="photo" role="img" aria-label="Bright green cannabis leaf"></div><h3>No Qualification? No Fee.</h3><p>Lorem ipsum dolor sit amet, consectetur adipiscing elit, sed do eiusmod tempor incididunt</p></div>
  <div class="card" style="left:775px"><div class="photo" role="img" aria-label="Hand holding a cannabis leaf"></div><h3>No Qualification? No Fee.</h3><p>Lorem ipsum dolor sit amet, consectetur adipiscing elit, sed do eiusmod tempor incididunt</p></div>
</section>

<footer class="site-footer" role="img" aria-label="Faint cannabis leaves behind the footer">
  <div class="foot-logo"><span class="logo-dot"></span><span class="logo-name">Arkansas<br>Orlow Wellness<br>Group</span></div>
  <p class="foot-about">Neque porro quisquam est qui dolorem ipsum quia dolor sit amet, consectetur, adipisci velit.</p>
  <h4 style="left:410px">Quick Links</h4>
  <ul class="links"><li>Home</li><li>About</li><li>Qualify</li><li>Appointments</li><li>FAQ</li><li>News</li><li>Contact</li></ul>
  <h4 style="left:550px">Contact Us</h4>
  <div class="contact">
    <div><svg width="18" height="18" viewBox="0 0 18 18" fill="#fff"><path d="M9 1a6 6 0 0 0-6 6c0 4.5 6 10 6 10s6-5.5 6-10a6 6 0 0 0-6-6zm0 8.5A2.5 2.5 0 1 1 9 4.5a2.5 2.5 0 0 1 0 5z"/></svg>123 Lorem Ipsum New York City</div>
    <div><svg width="18" height="18" viewBox="0 0 18 18" fill="none" stroke="#fff" stroke-width="1.6"><rect x="1.5" y="4" width="15" height="10" rx="1"/><path d="M2 5l7 5 7-5"/></svg>support@orlowwellness.com</div>
    <div><svg width="18" height="18" viewBox="0 0 18 18" fill="#fff"><path d="M4 1.5l3 3.5-1.6 2a9 9 0 0 0 5.6 5.6l2-1.6 3.5 3-1.8 2.5C8 16 2 10 1.5 3.3z"/></svg>501-555-0142</div>
  </div>
  <h4 style="left:788px">Get in Touch</h4>
  <div class="field" style="left:788px;top:100px;width:86px">Name</div>
  <div class="field" style="left:880px;top:100px;width:86px">Email</div>
  <div class="field" style="left:972px;top:100px;width:86px">Phone</div>
  <div class="field" style="left:788px;top:144px;width:270px;height:112px">Message</div>
  <div class="subscribe">Subscribe</div>
</footer>

<div class="bottom-bar">
  <p>Copyright © 2019 Arkansas Orlow Wellness Group</p>
  <span class="social" style="left:920px"></span>
  <span class="social" style="left:960px"></span>
  <span class="social" style="left:1000px"></span>
</div>

</body>
</html>
```